New Business Card Design Project

I would like my card design to look exactly like the logo, design, layout, and print of the current attached file. The only change I would like made would be for the print to say THE KMW GROUP instead of THE HALLORAN GROUP. Basically, just replace his group name with my group name. I would also like the backgroud to be the same texture and color as the attached file. I love the dark blue lettering and house logo on the card.

I am completely open to the rest of the card design. I just want something clean and simple. Only basic contact info required on the card. Maybe just name: Kyle M Warrick and cell # 555.914.2087 and email kyle@orchidhomesagent.com

```html
<!DOCTYPE html>
<html lang="en">
<head>
<meta charset="utf-8">
<title>The KMW Group – Business Card</title>
<link rel="stylesheet" href="https://fonts.googleapis.com/css2?family=Open+Sans:wght@400&family=Arimo:wght@400&display=swap">
<style>
  :root {
    --page: #ffffff;
    --card: #efefed;
    --navy: #0f0f24;
    --light: #ffffff;
  }
  * { margin: 0; padding: 0; box-sizing: border-box; }
  html, body {
    width: 1200px;
    height: 1000px;
    overflow: hidden;
    background: var(--page);
  }
  .card {
    position: absolute;
    left: 173px;
    top: 245px;
    width: 855px;
    height: 512px;
    background: radial-gradient(ellipse at 50% 45%, #f3f3f1 0%, var(--card) 100%);
  }
  .brand {
    position: absolute;
    left: 280px;
    top: 187px;
    display: flex;
    align-items: center;
    gap: 50px;
  }
  .brand-square {
    width: 108px;
    height: 108px;
    background: var(--navy);
  }
  .brand-name {
    font-family: "Open Sans", sans-serif;
    font-weight: 400;
    font-size: 31px;
    line-height: 40px;
    letter-spacing: 7px;
    color: var(--navy);
  }
  .contact-band {
    position: absolute;
    left: 0;
    top: 412px;
    width: 100%;
    height: 48px;
    background: var(--navy);
    color: var(--light);
    font-family: "Arimo", sans-serif;
    font-size: 19px;
  }
  .contact-item {
    position: absolute;
    top: 0;
    height: 48px;
    display: flex;
    align-items: center;
    gap: 8px;
  }
  .contact-item svg { display: block; }
  .contact-name { left: 70px; }
  .contact-phone { left: 307px; }
  .contact-email { left: 564px; }
</style>
</head>
<body>
  <div class="card">
    <div class="brand">
      <div class="brand-square"></div>
      <div class="brand-name">THE<br>KMW<br>GROUP</div>
    </div>

    <div class="contact-band">
      <div class="contact-item contact-name">
        <svg width="26" height="26" viewBox="0 0 26 26" fill="none" stroke="#fff" stroke-width="1.6">
          <circle cx="13" cy="13" r="11.5"/>
          <circle cx="13" cy="10.5" r="3.8"/>
          <path d="M6 20.5c1.8-3 4.2-4.3 7-4.3s5.2 1.3 7 4.3"/>
        </svg>
        <span>Kyle M Warrick</span>
      </div>
      <div class="contact-item contact-phone">
        <svg width="26" height="26" viewBox="0 0 26 26" fill="none" stroke="#fff" stroke-width="1.6">
          <circle cx="13" cy="13" r="11.5"/>
          <path d="M9 7.5l2 3-1.3 1.4c.8 1.8 2.2 3.2 4 4l1.4-1.3 3 2-1.3 2c-4.6-.4-8.8-4.6-9.2-9.2z" fill="#fff" stroke="none"/>
        </svg>
        <span>(555)-914-2087</span>
      </div>
      <div class="contact-item contact-email">
        <svg width="28" height="22" viewBox="0 0 28 22" fill="none" stroke="#fff" stroke-width="1.8">
          <rect x="1" y="1" width="26" height="20"/>
          <path d="M1 1l13 11L27 1M1 21l10-9M27 21l-10-9"/>
        </svg>
        <span>kyle@orchidhomesagent.com</span>
      </div>
    </div>
  </div>
</body>
</html>
```